Beekeeper needs box/label design for honey/CBD and other honey-related products

We need a box (or label) design for a beekeeping company in Virginia called Larkmoor Hollow Farm. Our products will include honey mixed with CBD oil and other essential oils (vanilla, lavender, etc).The box design should be scalable to include several different honey/oil products. We would like to incorporate our current farm logo into the design. Here is a link to a honey producing company with a series of products using their honey mixed with certain oils. It's a good reference of what type box/label design we would like (https://pipandwrenly.co/pages/honey).

Target Market(s)

Retail stores and consumers

Requirements
Must have
• Larkmoor Hollow Farm name and logo

```html
<!DOCTYPE html>
<html lang="en">
<head>
<meta charset="utf-8">
<title>Larkmoor Hollow Farm – Hemp + Lavender Blended Honey Label</title>
<link rel="stylesheet" href="https://fonts.googleapis.com/css2?family=Cinzel:wght@400;700&family=Marcellus&display=swap">
<style>
  :root {
    --backdrop: #d6c6b8;
    --label-white: #ffffff;
    --olive: #6d6a29;
    --lime: #b5c030;
    --lime-soft: #cdd588;
    --rule-grey: #5a5a55;
    --ink: #2b2b26;
  }
  * { margin: 0; padding: 0; box-sizing: border-box; }
  html, body {
    width: 1200px; height: 779px; overflow: hidden;
    background: var(--backdrop);
  }
  .label {
    position: absolute; left: 233px; top: 30px;
    width: 733px; height: 720px;
    background: var(--label-white);
    box-shadow: 0 2px 10px rgba(0,0,0,0.08);
  }
  .brand-mark {
    position: absolute; left: 278px; top: 88px;
    width: 176px; height: 176px;
    border: 5px solid var(--olive);
  }
  .brand-name {
    position: absolute; left: 0; right: 0; top: 292px;
    text-align: center;
    font-family: "Marcellus", serif;
    font-size: 38px; letter-spacing: 1px;
    color: var(--olive);
    text-transform: uppercase;
  }
  .divider {
    position: absolute; left: 180px; top: 395px;
    width: 367px; height: 2px; background: var(--rule-grey);
  }
  .product-title {
    position: absolute; left: 180px; top: 412px; width: 367px;
    font-family: "Cinzel", serif; font-weight: 700;
    color: var(--lime);
  }
  .product-title .flavour {
    display: block; font-size: 27px; letter-spacing: 1px;
    text-align: justify; text-align-last: justify; line-height: 34px;
  }
  .product-title .kind {
    display: flex; justify-content: space-between; align-items: center;
  }
  .product-title .blended {
    font-size: 15px; letter-spacing: 1px;
    border-bottom: 2px solid var(--lime); padding-bottom: 2px;
  }
  .product-title .honey {
    font-size: 44px; letter-spacing: 2px; line-height: 44px;
  }
  .botanical-art {
    position: absolute; left: 248px; top: 528px;
    width: 232px; height: 146px;
    background: radial-gradient(ellipse at 50% 75%, var(--lime-soft) 0%, #e4e8bd 55%, rgba(255,255,255,0) 78%);
  }
  .spec {
    position: absolute; top: 598px;
    font-family: "Cinzel", serif; font-weight: 700;
    font-size: 11px; line-height: 18px; color: var(--ink);
    text-align: center;
  }
  .spec.net-weight { left: 146px; }
  .spec.cbd-content { left: 512px; }
  .origin-band {
    position: absolute; left: 0; bottom: 0;
    width: 100%; height: 46px;
    background: var(--lime);
    display: flex; align-items: center; justify-content: center;
    font-family: "Cinzel", serif; font-weight: 700;
    font-size: 18px; letter-spacing: 1px;
    color: var(--label-white);
  }
</style>
</head>
<body>
  <main class="label">
    <div class="brand-mark" aria-hidden="true"></div>
    <h1 class="brand-name">Larkmoor Hollow Farm</h1>
    <div class="divider"></div>
    <h2 class="product-title">
      <span class="flavour">Hemp + Lavender</span>
      <span class="kind"><span class="blended">Blended</span><span class="honey">Honey</span></span>
    </h2>
    <div class="botanical-art" role="img" aria-label="Illustration of hemp leaves with lavender sprigs"></div>
    <p class="spec net-weight">NET WT.<br>16.OZ</p>
    <p class="spec cbd-content">500MG<br>OF CBD</p>
    <footer class="origin-band">VIRGINIA</footer>
  </main>
</body>
</html>
```